Museum quality exhibition portfolio

Create a museum-quality exhibition portfolio documenting the acquisition of several works by Danish artist Karen Vindahl.
This publication will be presented as an anniversary gift before the artwork arrives from Denmark.
The recipient should feel as though he has been invited into a private gallery to experience the collection before it enters his home.
This is not a coffee table book.
This is not a photo album.
This is not a scrapbook.
It should feel like a publication sold in the bookstore of a world-class Scandinavian museum. The copy is in the file COPY and CONTENT I will be printing only 5 copies of this and it's primarily for my Husband for our anniversary as I purchased these works of arts shown in the moon board attachments. I also need the final file that I can send to a printer who will print on high quality paper.

```html
<!DOCTYPE html>
<html lang="en">
<head>
<meta charset="utf-8">
<title>The Halvard Linde Collection — Exhibition Portfolio</title>
<link href="https://fonts.googleapis.com/css2?family=Jost:wght@300;400;500;600&family=Libre+Caslon+Text:wght@400&display=swap" rel="stylesheet">
<style>
  :root {
    --backdrop: #6b6c6b;
    --paper: #edeae2;
    --gold: #a57d3a;
    --ink: #4a4540;
    --ink-soft: #6a645d;
  }
  * { margin: 0; padding: 0; box-sizing: border-box; }
  html, body { width: 1200px; height: 2600px; overflow: hidden; background: var(--backdrop); }
  body { position: relative; font-family: "Jost", sans-serif; color: var(--ink); }

  .spread {
    position: absolute; left: 160px; width: 870px; height: 555px;
    background: var(--paper); overflow: hidden;
  }
  .spread--intro { top: 137px; }
  .spread--one { top: 720px; }
  .spread--two { top: 1302px; }
  .spread--three { top: 1885px; }

  .rule { position: absolute; height: 1.5px; background: var(--gold); }

  /* Intro spread */
  .intro-copy {
    position: absolute; left: 68px; top: 123px; width: 298px;
    font-family: "Libre Caslon Text", serif; font-size: 4.7px; line-height: 8.2px; color: var(--ink);
  }
  .intro-copy p { margin-bottom: 6.5px; }
  .section-title {
    position: absolute; left: 570px; top: 232px;
    font-family: "Jost", sans-serif; font-weight: 500; font-size: 27px; line-height: 30px;
    letter-spacing: 0.3px; color: var(--gold);
  }

  /* Folio */
  .folio {
    position: absolute; top: 530px; left: 18px;
    font-size: 5px; letter-spacing: 0.2px; color: var(--ink-soft);
    display: flex; align-items: baseline;
  }
  .folio .num { color: var(--gold); }
  .folio .line { display: inline-block; width: 12px; height: 0.6px; background: var(--gold); margin: 0 2px; }
  .folio--right { left: auto; right: 18px; }

  /* Work spreads */
  .work { position: absolute; left: 68px; width: 220px; }
  .work-number {
    font-weight: 300; font-size: 25px; line-height: 26px; color: var(--gold);
  }
  .work-number + .rule { position: static; display: block; width: 32px; margin-top: 6px; }
  .work-title {
    margin-top: 22px; font-weight: 600; font-size: 9.5px; letter-spacing: 0.3px; color: var(--gold);
  }
  .work-meta { margin-top: 14px; font-size: 5.7px; line-height: 8.6px; color: var(--ink-soft); }
  .work-meta h4 { font-weight: 600; font-size: 5.7px; color: var(--ink); }
  .work-meta .block { margin-bottom: 5px; }
  .work-meta p + p { margin-top: 6px; }

  .plate { position: absolute; top: 0; left: 435px; width: 435px; height: 555px; }
  .plate--walnut { background: linear-gradient(160deg, #7a5636 0%, #5e3f26 55%, #6e4c30 100%); }
  .plate--veneer { background: radial-gradient(ellipse at 52% 50%, #e8561c 0%, #c9762e 30%, #4d4b47 62%, #5a5957 100%); }
  .plate--sconce { background: radial-gradient(ellipse at 55% 48%, #c9a679 0%, #d9c2a0 32%, #f1efec 62%, #f4f3f1 100%); }
</style>
</head>
<body>

<section class="spread spread--intro">
  <span class="rule" style="left:68px; top:79px; width:35px;"></span>
  <div class="intro-copy">
    <p>There is one final detail that makes this collection unlike any other we have ever owned.</p>
    <p>The works themselves remain on exhibition in Denmark as you read these pages. They are still living the first chapter of their story before beginning the next chapter in our home. Several of the pieces are collaborations between Karen and Marianne, making them an even more meaningful expression of the friendship and creativity that brought us here in the first place.</p>
    <p>Before the artwork arrives, Karen has already sent us one small piece of the journey: an engraved spike that will ultimately become part of one of the finished works. On that spike she engraved our family's words. Enjoy the Journey, along with M&amp;P+B - Oskar, Peter, and Bramble - and the three Freedom Symbols that Marianne and Oskar first created together while designing one of Oskar's bracelets. One symbol represents each of us. What began years ago as a shared design between friends has now been lovingly carried forward by Karen, connecting our family, our friendships, and this collection in one beautiful gesture.</p>
    <p>That is why these pieces mean so much to us.</p>
    <p>They are not simply works of art.</p>
    <p>They are expressions of friendship.</p>
    <p>They are reminders that the most meaningful collections are not built around objects, but around people.</p>
    <p>Years from now, I know we will admire the craftsmanship, the beauty, and the artistry of every piece Karen has created.</p>
    <p>But I hope, even more than that, we will remember Marianne's friendship, Karen's generosity, the quiet moments in Copenhagen that first captured our imagination, and the extraordinary journey that brought these works, and these remarkable women, into our lives.</p>
  </div>
  <h1 class="section-title">THE<br>COLLECTION</h1>
  <span class="rule" style="left:570px; top:314px; width:62px;"></span>
  <div class="folio"><span class="num">6</span><span class="line"></span>THE HALVARD LINDE COLLECTION</div>
  <div class="folio folio--right"><span class="line"></span><span class="num">7</span></div>
</section>

<section class="spread spread--one">
  <div class="work" style="top:232px;">
    <div class="work-number">01</div>
    <span class="rule"></span>
    <h2 class="work-title">STILLWATER</h2>
    <div class="work-meta">
      <div class="block"><h4>Karen Vindahl</h4>Stained walnut with hand-forged iron wall mount, silver<br>Halvard Linde Collection<br>Acquired July 2026</div>
      <div class="block"><h4>Karen's Words</h4>[Insert Karen's artist statement / original description for this work.]</div>
      <div class="block"><h4>Peter's Reflection</h4>
        <p>Some works ask to be admired. Others quietly ask to become part of your life.</p>
        <p>Stillwater was one of those pieces. The first time we saw it, I was not thinking about where it would hang or whether it would fit our home. I simply knew it belonged with us. As I have come to know Karen, I have realized that this piece reflects something I admire deeply about her. She has an extraordinary ability to look beneath the surface, revealing beauty where others might only see imperfections. That perspective has become a beautiful reminder for me. The most meaningful things in life - friendships, love, family, and even the wood Karen transforms - often become more beautiful because of their history, not in spite of it.</p>
      </div>
    </div>
  </div>
  <div class="plate plate--walnut" role="img" aria-label="Engraved silver spike resting on a walnut board covered with a handwritten note"></div>
  <div class="folio"><span class="num">8</span><span class="line"></span>THE HALVARD LINDE COLLECTION</div>
</section>

<section class="spread spread--two">
  <div class="work" style="top:234px;">
    <div class="work-number">02</div>
    <span class="rule"></span>
    <h2 class="work-title">GRAIN OF LIGHT</h2>
    <div class="work-meta">
      <div class="block"><h4>Karen Vindahl</h4>Myrtle veneer, patinated iron, Campo del Cielo iron meteorite, LED<br>Halvard Linde Collection<br>Acquired July 2026</div>
      <div class="block"><h4>Karen's Words</h4>[Insert Karen's artist statement / original description for this work.]</div>
      <div class="block"><h4>Peter's Reflection</h4>
        <p>I think this piece speaks as much about time as it does about light.</p>
        <p>Karen has given new life to a sheet of veneer that waited more than a century for the right moment to reveal its beauty. She paired it with a fragment of iron meteorite that began its journey billions of years ago, and somehow those materials now tell a story that feels deeply personal to us. Most meaningful of all is the Freedom Symbol, a symbol that began as a conversation between Marianne and you and now continues through Karen's work. It reminds me that stories do not end when they are passed from one person to another. They grow richer with every hand they touch.</p>
      </div>
    </div>
  </div>
  <div class="plate plate--veneer" role="img" aria-label="Illuminated wall light of myrtle veneer glowing red-orange inside a dark iron frame"></div>
  <div class="folio"><span class="num">10</span><span class="line"></span>THE HALVARD LINDE COLLECTION</div>
</section>

<section class="spread spread--three">
  <div class="work" style="top:233px;">
    <div class="work-number">03</div>
    <span class="rule"></span>
    <h2 class="work-title">ELLMORE SCONCE #01</h2>
    <div class="work-meta">
      <div class="block"><h4>Karen Vindahl</h4>Myrtle veneer or Flamed Birch veneer, forged iron, shellac with residual studio materials<br>Halvard Linde Collection<br>Acquired July 2026</div>
      <div class="block"><h4>Karen's Words</h4>[Insert Karen's artist statement / original description for this work.]</div>
      <div class="block"><h4>Peter's Reflection</h4>
        <p>This light reminds me that beauty is often revealed gradually.</p>
        <p>Unlit, it is quiet and understated. When illuminated, the wood seems to come alive, revealing patterns that were always there, simply waiting to be seen. I love that metaphor because it reminds me of the friendships that brought these pieces into our lives. What began years ago with Marianne eventually led us to Karen, and over time those relationships have revealed a depth we could never have imagined. Every time this light is switched on, I hope it reminds us that the most meaningful things in life often reveal themselves slowly, one layer at a time.</p>
      </div>
    </div>
  </div>
  <div class="plate plate--sconce" role="img" aria-label="Cylindrical burl veneer wall sconce held by a forged iron band against a white wall"></div>
  <div class="folio"><span class="num">12</span><span class="line"></span>THE HALVARD LINDE COLLECTION</div>
</section>

</body>
</html>
```